Vell Studio - Lash Serum Packaging

Need Packaging done for this Lash Serum for a brand called "Vell Studio". The bottle will remain black but the box can be any color. This will be for a 3ml bottle. Give me different options for packaging that is minimalist and clean for this brand that makes it look expensive and make people want to buy.

```html
<!DOCTYPE html>
<html lang="en">
<head>
<meta charset="UTF-8">
<title>Vell Studio – Lash &amp; Brow Serum Packaging</title>
<link href="https://fonts.googleapis.com/css2?family=Montserrat:wght@400;500;600&family=Playfair+Display:wght@400;500&display=swap" rel="stylesheet">
<style>
  :root {
    --canvas: #ece3da;
    --ink-black: #141414;
    --marble-light: #efe5dc;
    --marble-mid: #dccbbb;
    --marble-warm: #e6d6c6;
    --white: #ffffff;
    --copper-light: #e3a878;
    --copper: #b8743f;
    --copper-deep: #7a4322;
    --label-brown: #b07a52;
  }
  * { margin: 0; padding: 0; box-sizing: border-box; }
  html, body { width: 1200px; height: 2340px; overflow: hidden; }
  body {
    background: var(--canvas);
    font-family: "Montserrat", sans-serif;
    position: relative;
  }
  .dieline-set {
    position: absolute;
    top: 560px;
    left: 20px;
    width: 1160px;
    display: flex;
    gap: 40px;
  }
  .panel-group { width: 360px; display: flex; flex-direction: column; align-items: center; }
  .panel {
    position: relative;
    width: 360px;
    height: 850px;
    overflow: hidden;
    box-shadow: 0 10px 30px rgba(90, 60, 40, 0.18);
  }
  .panel--bottle { background: var(--ink-black); }
  .marble {
    position: absolute; inset: 0;
    background:
      linear-gradient(155deg, transparent 30%, rgba(255,255,255,0.35) 38%, transparent 46%),
      linear-gradient(120deg, transparent 55%, rgba(190,165,140,0.25) 62%, transparent 70%),
      linear-gradient(180deg, var(--marble-light) 0%, var(--marble-warm) 55%, var(--marble-mid) 100%);
  }
  .brand-name {
    position: absolute;
    top: 58px; left: 0; right: 0;
    text-align: center;
    color: var(--white);
    font-weight: 600;
    font-size: 22px;
    letter-spacing: 3px;
  }
  .product-title {
    position: absolute;
    top: 150px;
    left: 50%;
    transform: translateX(-50%);
    writing-mode: vertical-rl;
    color: var(--white);
    font-weight: 500;
    font-size: 34px;
    line-height: 1.15;
    display: flex;
    align-items: flex-start;
  }
  .product-title .rule {
    display: block;
    width: 1.5px;
    height: 150px;
    margin-right: 14px;
    background: rgba(255,255,255,0.7);
  }
  .wordmark {
    position: absolute;
    left: 0; right: 0; bottom: 10px;
    font-family: "Playfair Display", serif;
    font-weight: 400;
    font-size: 250px;
    line-height: 0.78;
    text-align: center;
    letter-spacing: -14px;
    background: linear-gradient(160deg, var(--copper-light) 0%, var(--copper) 45%, var(--copper-deep) 100%);
    -webkit-background-clip: text;
    background-clip: text;
    color: transparent;
  }
  .wordmark span { display: block; }
  .side-stack {
    position: absolute;
    top: 140px;
    left: 50%;
    transform: translateX(-50%);
    writing-mode: vertical-rl;
    display: flex;
    align-items: center;
    color: var(--white);
  }
  .side-stack .brand { font-weight: 600; font-size: 24px; letter-spacing: 3px; }
  .side-stack .rule { width: 1.5px; height: 40px; background: rgba(255,255,255,0.8); margin: 0 12px; }
  .side-stack .title { font-weight: 500; font-size: 38px; margin-top: 18px; }
  .panel-label {
    margin-top: 46px;
    color: var(--label-brown);
    font-weight: 600;
    font-size: 40px;
    letter-spacing: 2px;
  }
</style>
</head>
<body>
  <main class="dieline-set">
    <section class="panel-group">
      <div class="panel panel--bottle">
        <div class="brand-name">VELL STUDIO</div>
        <div class="product-title"><span>Lash &amp; Brow</span><span>Serum</span><span class="rule"></span></div>
        <div class="wordmark"><span>LA</span><span>SH</span></div>
      </div>
      <div class="panel-label">BOTTLE</div>
    </section>

    <section class="panel-group">
      <div class="panel panel--side">
        <div class="marble" role="img" aria-label="Soft beige marble texture"></div>
        <div class="side-stack">
          <span class="brand">VELL STUDIO</span>
          <span class="title">Lash &amp; Brow Serum</span>
        </div>
      </div>
      <div class="panel-label">SIDE</div>
    </section>

    <section class="panel-group">
      <div class="panel panel--front">
        <div class="marble" role="img" aria-label="Soft beige marble texture"></div>
        <div class="brand-name">VELL STUDIO</div>
        <div class="product-title"><span>Lash &amp; Brow</span><span>Serum</span><span class="rule"></span></div>
        <div class="wordmark"><span>LA</span><span>SH</span></div>
      </div>
      <div class="panel-label">FRONT</div>
    </section>
  </main>
</body>
</html>
```